Logo for a small law firm
phrase "Trial Lawyers" should appear
Professional
Colby, Fenwick & Lusk
R. Tomasz Colby
3817 SW 58th Avenue Suite 314 Miami, Florida 33155
tomasz@colbylegal.net
The name of the firm should appear at the top and the phrase "Trial Lawyers" below it
rtomaszcolby rtomaszcolby
Yes, of course. The name is Colby, Fenwick & Lusk. I am looking for a professional business logo/tradename for use on all stationery.
VelunoStudioWorks VelunoStudioWorks
Hi Sir/Madam, Can you please tell me the firm name which you want to put in the logo and which kind of logo you want? Thnx.

```html
<!DOCTYPE html>
<html lang="en">
<head>
<meta charset="utf-8">
<title>Colby, Fenwick &amp; Lusk — Business Card</title>
<link href="https://fonts.googleapis.com/css2?family=Montserrat:wght@400;500&display=swap" rel="stylesheet">
<style>
  :root {
    --navy: #14254a;
    --navy-deep: #0f1d3c;
    --gold: #e39b2c;
    --paper: #ffffff;
    --paper-shade: #eef0f3;
    --ink-light: #e8ecf4;
    --backdrop: #d9dadd;
  }
  html, body {
    margin: 0;
    width: 1200px;
    height: 904px;
    overflow: hidden;
    background: var(--backdrop);
  }
  .canvas {
    position: relative;
    width: 1200px;
    height: 904px;
  }
  .card {
    position: absolute;
    left: 250px;
    width: 700px;
    height: 400px;
    overflow: hidden;
    box-shadow: 0 6px 18px rgba(0,0,0,0.18);
  }
  .card--back { top: 36px; background: linear-gradient(135deg, var(--navy) 0%, var(--navy-deep) 100%); }
  .card--front { top: 468px; background: var(--navy); }

  .firm-name {
    text-align: center;
    font-family: "Montserrat", sans-serif;
  }
  .firm-name__title {
    font-weight: 500;
    font-size: 28px;
    letter-spacing: 0.5px;
    margin: 0 0 10px;
  }
  .firm-name__tagline {
    font-weight: 400;
    font-size: 20px;
    margin: 0;
  }
  .card--back .firm-name {
    position: absolute;
    left: 0; right: 0; top: 160px;
  }
  .card--back .firm-name__title { color: var(--paper); }
  .card--back .firm-name__tagline { color: var(--ink-light); }

  .front__top {
    position: absolute;
    left: 0; top: 0;
    width: 700px; height: 190px;
    background: linear-gradient(180deg, var(--paper) 0%, var(--paper-shade) 100%);
  }
  .front__stripe {
    position: absolute;
    left: 0; top: 190px;
    width: 700px; height: 4px;
    background: var(--gold);
  }
  .front__top .firm-name {
    position: absolute;
    left: 0; right: 0; top: 60px;
  }
  .front__top .firm-name__title,
  .front__top .firm-name__tagline { color: var(--navy); }

  .holder {
    position: absolute;
    left: 40px; top: 318px;
    font-family: "Montserrat", sans-serif;
    font-size: 20px;
    color: var(--paper);
    margin: 0;
  }
  .divider {
    position: absolute;
    left: 372px; top: 222px;
    width: 1px; height: 150px;
    background: var(--ink-light);
    opacity: 0.7;
  }
  .contact {
    position: absolute;
    left: 392px; top: 222px;
    font-family: "Montserrat", sans-serif;
    font-size: 15px;
    line-height: 22px;
    color: var(--ink-light);
  }
  .contact__address { margin: 0 0 12px; }
  .contact__line {
    display: flex;
    align-items: center;
    gap: 10px;
    margin: 0 0 4px;
  }
  .contact__icon { width: 16px; height: 16px; flex: none; }
</style>
</head>
<body>
<div class="canvas">

  <section class="card card--back">
    <div class="firm-name">
      <p class="firm-name__title">Colby, Fenwick &amp; Lusk</p>
      <p class="firm-name__tagline">Trial Lawyers</p>
    </div>
  </section>

  <section class="card card--front">
    <div class="front__top">
      <div class="firm-name">
        <p class="firm-name__title">Colby, Fenwick &amp; Lusk</p>
        <p class="firm-name__tagline">Trial Lawyers</p>
      </div>
    </div>
    <div class="front__stripe"></div>

    <p class="holder">R. Tomasz Colby</p>
    <div class="divider"></div>

    <div class="contact">
      <p class="contact__address">3817 SW 58th Avenue<br>Suite 314<br>Miami, Florida 33155</p>
      <p class="contact__line">
        <svg class="contact__icon" viewBox="0 0 16 16" aria-hidden="true">
          <circle cx="8" cy="8" r="8" fill="#e39b2c"/>
          <path d="M5.2 4.2l1.4-.4 1 2.2-.9.7c.4.9 1.1 1.6 2 2l.7-.9 2.2 1-.4 1.4c-3 .3-6.3-3-6-6z" fill="#14254a"/>
        </svg>
        (305) 555-0148
      </p>
      <p class="contact__line">
        <svg class="contact__icon" viewBox="0 0 16 16" aria-hidden="true">
          <circle cx="8" cy="8" r="8" fill="#e39b2c"/>
          <rect x="4" y="5.2" width="8" height="5.6" rx="0.6" fill="#14254a"/>
          <path d="M4.3 5.6L8 8.4l3.7-2.8" stroke="#e39b2c" stroke-width="0.9" fill="none"/>
        </svg>
        tomasz@colbylegal.net
      </p>
    </div>
  </section>

</div>
</body>
</html>
```